Vorn Staffing Full Length Retractable Office Banner

I need a design for a full-length retractable banner and A-Frame Sign for each of my offices. I have included designs that have been incorporated into a poster and tri-fold as a sample. I would like to see a colorful eyecatching banner that focuses on people. Would like to see some diversity with men and woman and different races.
Vorn Staffing is a light industrial staffing firm. www.VornStaffing.example

Target Market(s)

Job seekers looking for employment

Industry/Entity Type

Staffing / Recruiting

Font styles to use
Other font styles liked:
• Professional yet fun

Requirements
Must have
• Eye catching design with young hip vibe.
Nice to have
• primary colors with light industrial type jobs

```html
<!DOCTYPE html>
<html lang="en">
<head>
<meta charset="utf-8">
<title>Vorn Staffing – Retractable Banner</title>
<link href="https://fonts.googleapis.com/css2?family=Oswald:wght@300;400;600&family=Poppins:wght@300;400&family=Roboto:wght@400&display=swap" rel="stylesheet">
<style>
  :root {
    --stage: #656565;
    --navy: #2b2860;
    --red: #e3241f;
    --green: #1b6e33;
    --white: #ffffff;
    --mist-top: #eef0f1;
    --mist-bottom: #dfe2e4;
  }
  html, body {
    margin: 0;
    padding: 0;
    width: 1200px;
    height: 930px;
    overflow: hidden;
    background: var(--stage);
  }
  .banner {
    position: absolute;
    left: 413px;
    top: 25px;
    width: 374px;
    height: 880px;
    display: block;
  }
  .brand-name {
    font-family: "Poppins", sans-serif;
    font-weight: 400;
    fill: var(--navy);
  }
  .headline {
    font-family: "Oswald", sans-serif;
    fill: var(--white);
    text-anchor: middle;
  }
  .headline-strong { font-weight: 600; }
  .headline-light { font-weight: 300; }
  .web-address {
    font-family: "Roboto", sans-serif;
    font-weight: 400;
    fill: var(--white);
    letter-spacing: 2.4px;
    text-anchor: middle;
  }
</style>
</head>
<body>
<svg class="banner" viewBox="0 0 440 1035" xmlns="http://www.w3.org/2000/svg">
  <defs>
    <linearGradient id="office-mist" x1="0" y1="0" x2="0" y2="1">
      <stop offset="0" stop-color="var(--mist-top)"/>
      <stop offset="0.5" stop-color="#d6d9dc"/>
      <stop offset="1" stop-color="var(--mist-bottom)"/>
    </linearGradient>
  </defs>

  <rect class="banner-base" width="440" height="1035" fill="var(--white)"/>

  <rect class="team-photo" x="0" y="0" width="440" height="540" fill="url(#office-mist)"
        role="img" aria-label="Photo of a diverse group of men and women standing together in a bright office"/>

  <path class="sweep-white" d="M0 351 C60 340 110 390 144 426 C200 500 300 540 440 430 L440 1035 L0 1035 Z" fill="var(--white)"/>

  <path class="wave-red" d="M144 426 C190 460 240 470 284 456 C350 430 400 340 440 266 L440 441 C390 500 320 540 254 528 C200 515 170 470 144 426 Z" fill="var(--red)"/>

  <path class="edge-green" d="M440 531 C420 590 400 630 384 661 L440 741 Z" fill="var(--green)"/>

  <path class="panel-navy" d="M0 681 C70 730 150 750 214 744 C290 737 340 700 384 666 C405 652 425 652 440 656 L440 1035 L0 1035 Z" fill="var(--navy)"/>

  <path class="footer-red" d="M0 936 C60 940 110 986 170 986 C240 986 280 941 334 941 C380 941 410 952 440 956 L440 1035 L0 1035 Z" fill="var(--red)"/>

  <!-- brand -->
  <circle class="brand-dot" cx="52" cy="626" r="11" fill="var(--navy)"/>
  <text class="brand-name" x="74" y="640" font-size="40" textLength="280" lengthAdjust="spacingAndGlyphs">Vorn Staffing</text>

  <!-- headline -->
  <text class="headline headline-strong" x="222" y="814" font-size="66">CONNECTING</text>
  <text class="headline" x="222" y="860" font-size="40"><tspan class="headline-strong">GREAT</tspan> <tspan class="headline-light">PEOPLE</tspan></text>
  <text class="headline headline-light" x="222" y="890" font-size="24">WITH</text>
  <text class="headline headline-strong" x="222" y="930" font-size="35">GREAT ORGANIZATIONS!</text>

  <text class="web-address" x="220" y="1014" font-size="13">www.VornStaffing.example</text>
</svg>
</body>
</html>
```